K&T Fixit and Rebuild general contracting business card design

I already have a logo that I want to use and I need a card that uses that logo and color scheme on the front with the address phone numbers and email and on the back a place for technicians to write in their name and phone number when they hand it out. It will need the License number of License #KTFXTRB318QN.
It should say General Contractor under the company name. The address is
4417 NE 3rd Ave, Ste D246
Vancouver, WA 98612
www.kandtfixitandrebuild.example
office@kandtfixitandrebuild.example
360-555-0182 is the telephone number
360-555-0149 is the fax number

Target Market(s)

Homeowners needing remodel work or repairs in their home.

Industry/Entity Type

Construction

Contact Information for Business Card

Business name, address, phone number, license number, fax number, email, and website on the front and a place to fill in technician's name and number

Font styles to use
Serif

Requirements
Must have
• Business name, address, phone number, license number, fax number, email, and website on the front and a place to fill in technician's name and number
Nice to have
• I uploaded an example of a front that is good.
Should not have
• Froo froo or extra embellishments.

```html
<!DOCTYPE html>
<html lang="en">
<head>
<meta charset="utf-8">
<title>K&amp;T Fixit and Rebuild — Business Card</title>
<link rel="stylesheet" href="https://fonts.googleapis.com/css2?family=Michroma&family=Montserrat:wght@400;500;600&display=swap">
<style>
  :root {
    --page: #e9e6e2;
    --card-white: #f7f6f4;
    --copper: #a9582e;
    --name-cream: #f3e2d6;
    --wood-light: #9a6a4b;
    --wood-dark: #6f4630;
    --ink: #1f1a17;
    --watermark: #ece3dc;
    --box-line: #9c6a50;
  }
  * { box-sizing: border-box; margin: 0; padding: 0; }
  html, body { width: 1200px; height: 875px; overflow: hidden; }
  body {
    background: var(--page);
    font-family: "Montserrat", sans-serif;
    color: var(--ink);
    position: relative;
  }
  .card {
    position: absolute;
    left: 250px;
    width: 700px;
    height: 400px;
    border-radius: 22px;
    overflow: hidden;
    box-shadow: 0 6px 18px rgba(0,0,0,0.18);
  }
  .card--logo { top: 25px; }
  .card--details { top: 450px; background: var(--card-white); }

  /* Front side */
  .wood-surface {
    position: absolute; inset: 0;
    background: linear-gradient(100deg, var(--wood-light) 0%, #8a5c3f 45%, var(--wood-dark) 100%);
  }
  .company-name {
    position: absolute;
    left: 0; right: 0; top: 176px;
    text-align: center;
    font-family: "Montserrat", sans-serif;
    font-weight: 600;
    font-size: 40px;
    line-height: 48px;
    color: var(--name-cream);
  }

  /* Details side */
  .title-band { position: absolute; left: 0; top: 62px; }
  .title-band__name {
    position: absolute; left: 28px; top: 82px;
    font-family: "Michroma", sans-serif;
    font-weight: 400;
    font-size: 23px; line-height: 30px; color: #fff; letter-spacing: 1px;
  }
  .title-band__role {
    position: absolute; left: 36px; top: 116px;
    font-size: 15px; font-weight: 500; color: var(--name-cream); letter-spacing: 0.5px;
  }
  .watermark {
    position: absolute; left: 420px; top: 176px;
    font-family: "Montserrat", sans-serif;
    font-weight: 600; font-size: 38px; line-height: 46px;
    color: var(--watermark);
  }
  .details { position: absolute; left: 50px; top: 168px; font-size: 16px; line-height: 1.45; }
  .details__license { margin-bottom: 12px; }
  .details__address { margin-bottom: 12px; }
  .contact-list { list-style: none; }
  .contact-list li { display: flex; align-items: center; gap: 10px; height: 24px; }
  .contact-list svg { width: 16px; height: 16px; flex: none; }
  .fill-in {
    position: absolute; right: 28px; top: 22px;
    width: 116px; height: 356px;
    border: 1px solid var(--box-line);
    border-radius: 10px;
    display: flex; justify-content: center;
    padding: 18px 0;
  }
  .fill-in__fields {
    writing-mode: vertical-rl;
    font-size: 17px; line-height: 34px;
  }
  .fill-in__dots { letter-spacing: 1px; color: #444; }
</style>
</head>
<body>

<section class="card card--logo" aria-label="Card front">
  <div class="wood-surface" role="img" aria-label="Warm brown wood plank texture background"></div>
  <p class="company-name">K&amp;T Fixit and Rebuild</p>
</section>

<section class="card card--details" aria-label="Card back">
  <p class="watermark" aria-hidden="true">K&amp;T Fixit<br>and Rebuild</p>
  <svg class="title-band" width="400" height="90" viewBox="0 0 400 90" aria-hidden="true">
    <polygon points="0,0 395,0 355,90 0,90" fill="var(--copper)"/>
  </svg>
  <h1 class="title-band__name">FIXIT &amp; REBUILD</h1>
  <p class="title-band__role">General Contractor</p>

  <div class="details">
    <p class="details__license">License #KTFXTRB318QN</p>
    <p class="details__address">4417 NE 3rd Ave, Ste D246<br>Vancouver, WA 98612</p>
    <ul class="contact-list">
      <li>
        <svg viewBox="0 0 16 16"><path d="M3 2h3l1 3-2 1c1 2 2 3 4 4l1-2 3 1v3c0 1-1 2-2 2C6 14 2 10 2 4c0-1 0-2 1-2z" fill="var(--copper)"/></svg>
        360-555-0182
      </li>
      <li>
        <svg viewBox="0 0 16 16"><rect x="4" y="1" width="8" height="4" fill="var(--copper)"/><rect x="1" y="6" width="14" height="6" rx="1" fill="var(--copper)"/><rect x="4" y="10" width="8" height="5" fill="#fff" stroke="var(--copper)" stroke-width="1.5"/></svg>
        360-555-0149
      </li>
      <li>
        <svg viewBox="0 0 16 16"><rect x="1" y="3" width="14" height="10" rx="1" fill="var(--copper)"/><path d="M1.5 3.5 8 9l6.5-5.5" fill="none" stroke="#fff" stroke-width="1.3"/></svg>
        office@kandtfixitandrebuild.example
      </li>
      <li>
        <svg viewBox="0 0 16 16"><circle cx="8" cy="8" r="7" fill="var(--copper)"/><path d="M1 8h14M8 1c-3 3-3 11 0 14M8 1c3 3 3 11 0 14" fill="none" stroke="#fff" stroke-width="1"/></svg>
        www.kandtfixitandrebuild.example
      </li>
    </ul>
  </div>

  <div class="fill-in">
    <p class="fill-in__fields">
      Name: <span class="fill-in__dots">.............................</span><br>
      Contact: <span class="fill-in__dots">.........................</span>
    </p>
  </div>
</section>

</body>
</html>
```